Finance Broker helping people meet their personal and business goals

New business card design,
1st look at the old business card so this makes sense.
I DON'T want:
the subtext "For all your Rural and Commercial Finance".
I DON'T want the: "and Management Consultant" words
I DON'T want the old phone: 07 48213957
I DON'T want the fax number: 07 45826031
I DON'T want the email address: tallowcreek@brightlink.com.au
I DON'T want the flower
What I DO want
I DO want the mobile 0451 836 209 (in larger text)
I DO want:
My name: Dennis Harwell-Lowe
I DO want: Australian Credit Licence 529164 (Tallow Creek Pty Ltd)
I DO want: Principal Finance Broker
I DO want new email: dennis@plotnextstep.com.au
I DO want address: PO Box 928, Tully Qld 4854
I DO want the existing logo (PNS on existing card)

Target Market(s)

Business Borrowers, Home Purchasers, and People wanting to finance cars and plant and equipment

Industry/Entity Type

Financial Service

Contact Information for Business Card

See project description

Font styles to use
Serif

Colors

Designer to choose colors to be used in the design.

Requirements
Must have
• See project description
Nice to have
• Black and Yellow colours
Should not have
• See project description

```html
<!DOCTYPE html>
<html lang="en">
<head>
<meta charset="utf-8">
<title>Plot Next Step – Business Card</title>
<link rel="stylesheet" href="https://fonts.googleapis.com/css2?family=Tinos:wght@400;700&family=Arimo:wght@400;700&family=Roboto+Condensed:wght@300&display=swap">
<style>
  :root {
    --page: #f4f5f7;
    --card: #2b2a29;
    --yellow: #f8f23a;
    --white: #ffffff;
    --serif: "Tinos", "Times New Roman", serif;
    --sans: "Arimo", Arial, sans-serif;
    --numeral: "Roboto Condensed", "Arial Narrow", sans-serif;
  }
  * { box-sizing: border-box; margin: 0; padding: 0; }
  html, body { width: 1200px; height: 1000px; overflow: hidden; background: var(--page); }
  .canvas { position: relative; width: 1200px; height: 1000px; }

  .card {
    position: absolute; left: 293px; width: 614px; height: 375px;
    background: var(--card); color: var(--white);
  }
  .card--front { top: 108px; }
  .card--back { top: 517px; }

  .mark { display: flex; align-items: center; color: var(--yellow); font-family: var(--serif); font-weight: 400; }
  .mark__dot { border-radius: 50%; background: var(--yellow); flex: none; }

  .front-brand { position: absolute; left: 93px; top: 47px; display: flex; align-items: center; gap: 22px; }
  .front-brand .mark { gap: 8px; font-size: 40px; }
  .front-brand .mark__dot { width: 52px; height: 52px; }

  .wordmark__name { font-family: var(--serif); color: var(--yellow); line-height: 1; letter-spacing: -0.3px; }
  .wordmark__sub { font-family: var(--serif); color: var(--white); letter-spacing: 0.8px; line-height: 1; }
  .front-brand .wordmark__name { font-size: 29px; }
  .front-brand .wordmark__sub { font-size: 12.3px; margin-top: 4px; }

  .contact { position: absolute; left: 0; right: 0; top: 163px; text-align: center; font-family: var(--sans); }
  .contact__name { font-size: 22.5px; font-weight: 700; letter-spacing: 0.2px; line-height: 1; }
  .contact__role { font-size: 15.5px; color: var(--yellow); margin-top: 9px; line-height: 1; }
  .contact__licence { font-size: 14.2px; margin-top: 6px; line-height: 1; }
  .contact__phone { display: flex; justify-content: center; align-items: center; gap: 10px; margin-top: 18px;
    font-family: var(--numeral); font-weight: 300; font-size: 33px; line-height: 1; }
  .contact__phone svg { width: 18px; height: 28px; }
  .contact__lines { font-size: 14.2px; line-height: 18px; margin-top: 15px; }

  .back-mark { position: absolute; left: 0; right: 0; top: 93px; display: flex; justify-content: center; }
  .back-mark .mark { gap: 12px; font-size: 70px; }
  .back-mark .mark__dot { width: 86px; height: 86px; }

  .back-wordmark { position: absolute; left: 0; right: 0; top: 247px; text-align: center; }
  .back-wordmark .wordmark__name { font-size: 38px; }
  .back-wordmark .wordmark__sub { font-size: 16.5px; margin-top: 5px; }
</style>
</head>
<body>
<main class="canvas">
  <section class="card card--front" aria-label="Business card front">
    <div class="front-brand">
      <div class="mark"><span class="mark__dot"></span><span>PNS</span></div>
      <div class="wordmark">
        <div class="wordmark__name">Plot Next Step</div>
        <div class="wordmark__sub">A Member of the Tallow Creek Group</div>
      </div>
    </div>
    <div class="contact">
      <div class="contact__name">DENNIS HARWELL-LOWE</div>
      <div class="contact__role">PRINCIPAL FINANCE BROKER</div>
      <div class="contact__licence">Australian Credit Licence 529164 (Tallow Creek Pty Ltd)</div>
      <div class="contact__phone">
        <svg viewBox="0 0 18 28" aria-hidden="true">
          <rect x="1.5" y="1.5" width="15" height="25" rx="3" fill="none" stroke="#fff" stroke-width="2.4"/>
          <rect x="4.5" y="5" width="9" height="15" fill="#fff"/>
          <rect x="7" y="22" width="4" height="1.6" rx="0.8" fill="#fff"/>
        </svg>
        <span>0451 836 209</span>
      </div>
      <div class="contact__lines">
        <div>dennis@plotnextstep.com.au</div>
        <div>PO Box 928, Tully Qld 4854</div>
      </div>
    </div>
  </section>

  <section class="card card--back" aria-label="Business card back">
    <div class="back-mark">
      <div class="mark"><span class="mark__dot"></span><span>PNS</span></div>
    </div>
    <div class="back-wordmark">
      <div class="wordmark__name">Plot Next Step</div>
      <div class="wordmark__sub">A Member of the Tallow Creek Group</div>
    </div>
  </section>
</main>
</body>
</html>
```